依頼詳細
発泡スチロール製品の事例を紹介するリーフレットのデザインをお願い致します。
発泡スチロールの箱をいろいろな業種の方にご利用いただいております。いろいろな発泡スチロールの利用状況とお客様の声を今後DMとして発送を計画しております。
シリーズとして使えるようにしていきたいと考えております。今回は緑系統で、今後は色を替えることも想定してデザインをお願いできればと思います。
記載項目
社名、電話番号、ホームページアドレス、所在地
サイズ
A4
ページ数
片面
希望イメージ
シンプル 複雑
単色 カラフル
暗い 明るい
日常 高級
遊び心 厳粛
未来的 伝統的
女性的 男性的
希望する色
緑系、ロゴの色
納品ファイル
• イラストレーター形式 (.ai)
補足説明
ロゴデータはありません。添付書類参照下さい。
お世話になっております。コンペ参加者の皆様大変申し訳ありませんが、もう少し提案数が必要なため提案期日を10日延長いたしました。
現在参加されている方には大変申し訳ありませんがご理解いただきますようお願い申し上げます。
■ 選んだ理由

大変素晴らしいデザインありがとうございました。
お客様も大変悩まれておりましたが、大変気に入って頂けました。

■ 提案者全員のお礼・コメント

沢山のご提案ありがとうございました。
今後共デザインコンペを行ってまいりますのでよろしくお願いいたします。

```html
<!DOCTYPE html>
<html lang="ja">
<head>
<meta charset="utf-8">
<link href="https://fonts.googleapis.com/css2?family=Noto+Sans+JP:wght@400;500;700;900&family=Roboto+Condensed:wght@400;700&display=swap" rel="stylesheet">
<style>
:root{
  --green:#3d9a3a;
  --green-dark:#2d7e2c;
  --green-pale:#e9f4e4;
  --ink:#333;
  --accent:#c0392b;
  --white:#fff;
}
*{margin:0;padding:0;box-sizing:border-box}
html,body{width:846px;height:1200px;overflow:hidden;background:var(--white)}
body{font-family:"Noto Sans JP",sans-serif;color:var(--ink);position:relative}
.header{position:absolute;left:0;top:0;width:846px;height:96px;background:var(--green);display:flex;align-items:center;padding:0 28px}
.brand{display:flex;flex-direction:column;align-items:center;color:var(--white);width:90px}
.brand-mark{width:50px;height:50px;background:var(--white)}
.brand-name{font:700 15px "Roboto Condensed",sans-serif;letter-spacing:1px;margin-top:3px}
.header-title{font:700 50px "Roboto Condensed",sans-serif;color:var(--white);margin-left:22px;letter-spacing:1px}
.issue{position:absolute;right:30px;top:10px;width:62px;text-align:center;color:var(--white);font-family:"Roboto Condensed",sans-serif}
.issue-year{font-size:18px;border-bottom:1px solid var(--white);padding-bottom:2px}
.issue-no{font-size:40px;font-weight:700;line-height:1.1}
.title{position:absolute;left:28px;top:116px;font-weight:900;font-size:35px;line-height:1.3;color:var(--ink)}
.title-sub{position:absolute;left:28px;top:256px;font-size:14px}
.photo-main{position:absolute;left:330px;top:96px;width:516px;height:395px;background:linear-gradient(160deg,#f6f4ee,#e7e1d2 60%,#c9b98f)}
.photo-small{position:absolute;left:22px;top:290px;width:300px;height:185px;background:linear-gradient(160deg,#f8f6f1,#e6dcc4 60%,#b99b62)}
.lead{position:absolute;left:22px;top:505px;width:800px;font-weight:900;font-size:25px;line-height:1.4;color:var(--green-dark)}
.section{position:absolute;left:22px;width:802px;display:flex;background:var(--green-pale)}
.section-label{width:104px;background:var(--green);color:var(--white);display:flex;flex-direction:column;justify-content:center;align-items:center;text-align:center;flex-shrink:0}
.section-en{font:italic 700 14px "Roboto Condensed",sans-serif;color:#d8efcf}
.section-ja{font-weight:700;font-size:13px;line-height:1.4;margin-top:4px}
.section-body{padding:12px 16px;font-size:12.5px;line-height:1.75}
.section-body ul{list-style:none}
.section-body li::before{content:"■";color:var(--green);margin-right:3px}
.section-body em{font-style:normal;color:var(--accent)}
.request{top:585px;height:140px}
.suggestion{top:740px;height:118px}
.impressions{top:873px;height:170px}
.footer{position:absolute;left:0;top:1085px;width:846px;height:115px;background:var(--green);color:var(--white);display:flex;align-items:center;padding:0 28px}
.footer .brand{width:80px}
.footer .brand-mark{width:40px;height:40px}
.footer .brand-name{font-size:12px}
.company{margin-left:24px}
.company-name{font-size:22px;font-weight:700}
.company-addr{font-size:12px;margin-top:4px}
.contact{margin-left:auto;text-align:left}
.contact-lead{font-size:13px}
.contact-tel{font:700 34px "Roboto Condensed",sans-serif;line-height:1.1}
.contact-web{font-size:13px}
</style>
</head>
<body>
<header class="header">
  <div class="brand"><div class="brand-mark"></div><div class="brand-name">NORVEX</div></div>
  <div class="header-title">PRODUCT INFOMATION</div>
  <div class="issue"><div class="issue-year">2018</div><div class="issue-no">1</div></div>
</header>

<h1 class="title">アイス保冷用<br>発泡スチロール<br>販売事例</h1>
<p class="title-sub">(製品 緑ヶ丘牧場「雪華アイス」)</p>

<div class="photo-main" role="img" aria-label="白い発泡スチロール容器に入ったアイスカップ3個と商品パッケージの写真"></div>
<div class="photo-small" role="img" aria-label="アイスカップを3個収めた保冷用発泡スチロール箱の写真"></div>

<p class="lead">新商品の高級なアイスクリームを販売にともない、<br>保冷製が高く、高級感を持ったパッケージを採用したい。</p>

<section class="section request">
  <div class="section-label"><span class="section-en">Request</span><span class="section-ja">お客様からの<br>ご要望</span></div>
  <div class="section-body"><ul>
    <li>新商品のアイスクリームを開発中。</li>
    <li>そのアイスクリームは生乳やバニラなど素材にこだわった今までに無い高級なアイスクリームを販売したい。</li>
    <li>名前は「雪華アイス」で3個入りの発泡スチロール容器が必要。</li>
    <li>保冷性能が高く外観も高級感を持ったパッケージを採用したい。</li>
    <li>販売数量は特別なので予算は比較的大きいので型代などの経費はかけられない。</li>
  </ul></div>
</section>

<section class="section suggestion">
  <div class="section-label"><span class="section-en">Suggestion</span><span class="section-ja">ノルベックス<br>からの<br>ご提案</span></div>
  <div class="section-body">様々検討・考察を重ねた結果、下記のようにお客様にパッケージのご提案を致しました。<br>a) 中ふたについては中央は当社独自形状の一番美しく見える容器を選定<br>b) 外観については高級感を出すカラーのブラウン着色を選定</div>
</section>

<section class="section impressions">
  <div class="section-label"><span class="section-en">Impressions</span><span class="section-ja">お客様からの<br>声</span></div>
  <div class="section-body">「発泡スチロール容器が四角では面白味が無い」とのご意見を頂き、提出したサンプルが「雪華アイス」のコンセプトに合致していました。<br>提案にて発泡スチロール容器のブラウン色が高級感や木の箱のような落ち着いた雰囲気を感じ、中仕切りは真空で一体化し、アイスカップを美しく見せるものになり、高級感を演出することにつながっていったとのことでした。<br>また「<em>今回の採用は、ノルベックスから的確な提案力があるからこそ</em>」とのお言葉も頂きました。</div>
</section>

<footer class="footer">
  <div class="brand"><div class="brand-mark"></div><div class="brand-name">NORVEX</div></div>
  <div class="company">
    <div class="company-name">株式会社ノルベックス</div>
    <div class="company-addr">〒322-0000 栃木県鹿沼市緑町1番地</div>
  </div>
  <div class="contact">
    <div class="contact-lead">お問い合わせは</div>
    <div class="contact-tel">TEL.0289-00-1234</div>
    <div class="contact-web">http://www.norvex-ware.example/</div>
  </div>
</footer>
</body>
</html>
```